Commercial Waterproofing Modern Business Cards

We are a Commercial Waterproofing company. We do a variety of jobs on the exterior of buildings. We repel from the top or scaffold to reach the areas. Cut out and recaulk expansion joints and apply sealants, brick/concrete repairs, seal window frame perimeters, and much more. Our website is www.ledgecrestfix.com.
We are looking for a new business card design that would look more modern and cutting edge. We like the transparent paper and had thought about using our logo, but maybe pulling it apart to where the building part is kind of in the background. I have attached 2 different logos that we use regularly. We want the design to be a little funky, but professional at the same time. We really don't want the logo to be incorporated by itself, but you can use the logo and take out the buildings and just use the name or vice versa. Please don't just put the logo on the card and the words around that.

Target Market(s)

Property Managers/Building Maintenance

Industry/Entity Type

Business

Contact Information for Business Card

Daniel Trovato President
Office (919)555-4827
Mobile (919)555-9306

Font styles to use
Serif

Requirements
Must have
• Nice overall design, somehow pulling from the logo for the design
Nice to have
• Look artsy and modern with a nice quality paper
Should not have
• Too many words or distracting designs. The logo 'as is'

```html
<!DOCTYPE html>
<html lang="en">
<head>
<meta charset="UTF-8">
<title>LedgeCrest Fix — Business Card</title>
<link href="https://fonts.googleapis.com/css2?family=Source+Serif+4:opsz,wght@8..60,400;8..60,600;8..60,700&display=swap" rel="stylesheet">
<style>
  :root {
    --page-bg: #e9e7e4;
    --card-bg: #f7f6f4;
    --ink: #1f1f22;
    --brand-blue: #2f6fae;
    --accent-blue: #3f8fbf;
    --tone-blue: #6a9fd0;
    --tone-violet: #7f7bbd;
    --tone-deep: #5468ae;
    --divider: #3c7fb0;
  }
  html, body {
    margin: 0;
    padding: 0;
    width: 1200px;
    height: 970px;
    overflow: hidden;
    background: var(--page-bg);
  }
  .business-card {
    position: absolute;
    left: 100px;
    top: 207px;
    width: 1000px;
    height: 556px;
    background: var(--card-bg);
    box-shadow: 0 10px 30px rgba(0,0,0,0.15);
    overflow: hidden;
    font-family: 'Source Serif 4', Georgia, serif;
  }
  .tone-field {
    position: absolute;
    left: 0;
    width: 1000px;
  }
  .tone-field--top {
    top: 0;
    height: 90px;
    background: linear-gradient(90deg,
      rgba(247,246,244,0) 0%,
      rgba(127,123,189,0.25) 40%,
      rgba(106,159,208,0.7) 100%);
  }
  .tone-field--bottom {
    bottom: 0;
    height: 90px;
    background: linear-gradient(90deg,
      rgba(84,104,174,0.8) 0%,
      rgba(127,123,189,0.45) 50%,
      rgba(247,246,244,0) 100%);
  }
  .brand-block {
    position: absolute;
    left: 150px;
    top: 256px;
    display: flex;
    align-items: center;
    gap: 14px;
  }
  .brand-square {
    width: 24px;
    height: 24px;
    background: var(--brand-blue);
  }
  .brand-name {
    font-size: 36px;
    font-weight: 600;
    color: var(--brand-blue);
    white-space: nowrap;
  }
  .divider {
    position: absolute;
    left: 497px;
    top: 185px;
    width: 3px;
    height: 210px;
    background: var(--divider);
  }
  .contact-block {
    position: absolute;
    left: 529px;
    top: 172px;
  }
  .person-name {
    margin: 0;
    font-size: 46px;
    font-weight: 600;
    color: var(--ink);
    letter-spacing: 0.5px;
    line-height: 1.1;
    white-space: nowrap;
  }
  .person-title {
    margin: 2px 0 0;
    font-size: 24px;
    font-weight: 600;
    color: var(--accent-blue);
  }
  .phone-list {
    list-style: none;
    margin: 18px 0 0;
    padding: 0;
  }
  .phone-item {
    display: flex;
    align-items: center;
    gap: 16px;
    font-size: 25px;
    font-weight: 600;
    color: var(--ink);
    height: 44px;
  }
  .phone-icon {
    width: 24px;
    height: 24px;
    flex: none;
  }
</style>
</head>
<body>
  <div class="business-card">
    <div class="tone-field tone-field--top" role="img" aria-label="Soft blue and violet decorative band"></div>
    <div class="tone-field tone-field--bottom" role="img" aria-label="Soft blue and violet decorative band"></div>

    <div class="brand-block">
      <span class="brand-square"></span>
      <span class="brand-name">LedgeCrest Fix</span>
    </div>

    <div class="divider"></div>

    <div class="contact-block">
      <h1 class="person-name">Daniel Trovato</h1>
      <p class="person-title">President</p>
      <ul class="phone-list">
        <li class="phone-item">
          <svg class="phone-icon" viewBox="0 0 24 24" aria-label="Office">
            <path d="M2 9 C2 5 7 4 12 4 C17 4 22 5 22 9 L22 11 L17 11 L16 8 L8 8 L7 11 L2 11 Z" fill="var(--brand-blue)"/>
            <path d="M6 12 L18 12 L20 20 L4 20 Z" fill="var(--brand-blue)"/>
            <circle cx="12" cy="16" r="2.2" fill="#f7f6f4"/>
          </svg>
          <span>(919)555-4827</span>
        </li>
        <li class="phone-item">
          <svg class="phone-icon" viewBox="0 0 24 24" aria-label="Mobile">
            <rect x="6" y="2" width="12" height="20" rx="2" fill="none" stroke="var(--brand-blue)" stroke-width="2"/>
            <circle cx="12" cy="18.5" r="1.1" fill="var(--brand-blue)"/>
          </svg>
          <span>(919)555-9306</span>
        </li>
      </ul>
    </div>
  </div>
</body>
</html>
```